COMMERCIAL REAL ESTATE FLYER TEMPLATE

We need a template flyer designed that we can use for a current commercial real estate listing and subsequently use as a template for future listings. We have uploaded images and files to provide an example of an older flyer template we have used. If you have questions or would like to discuss, please contact us at Marty@TLVKE.com. Colors selected should be in line with our attached business card and logo design. Output should be 8.5" X 11".

Target Market(s)

Commercial Real Estate. NO RESIDENTIAL. Needs to have a professional commercial presentation with no reference to residential real estate.

Industry/Entity Type

Real Estate Agent

Font styles to use
Serif

Colors

Designer to choose colors to be used in the design.

Requirements
Must have
• MUST BE SAVED AND ADJUSTABLE IN ONE OF THE FOLLOWING FORMATES: MICROSOFT POWERPOINT, PUBLISHER OR WORD. THIS IS IMPORTANT SO OUR TEAM CAN EASILLY UPDATE TEMPLATE IN READILLY AVAILABLE PROGRAMS THAT ARE SIMPLE FOR TEAM MEMBERS TO USE.
Nice to have
• Needs to have first page template with header and footer displaying our logo, address, phone, email address and contact information for the listing agent. There need to be placeholders that can be easily adjusted based on specific listings. Placeholders will be used for pictures or aerials as the case requires. Needs to have a second page that has header and footer with a clean open block in the middle of the page so agents can customize with site specific details.
Should not have
• There should be no reference to residential. We are a commercial real estate organization that does not do any residential.

```html
<!DOCTYPE html>
<html lang="en">
<head>
<meta charset="utf-8">
<title>Commercial Flyer Template – Page Set</title>
<link href="https://fonts.googleapis.com/css2?family=Montserrat:wght@400;500;600;700&display=swap" rel="stylesheet">
<style>
:root{
  --red:#c1272d;
  --red-dark:#a51f25;
  --ink:#333;
  --muted:#666;
  --board:#1d1d1d;
  --paper:#fff;
  --sky:#a9c6e3;
  --plan-peach:#f6c9a3;
  --plan-blue:#b9dde6;
}
*{box-sizing:border-box;margin:0;padding:0}
html,body{width:1200px;height:1200px;overflow:hidden;background:var(--board);font-family:"Montserrat",sans-serif;color:var(--ink)}
.board{position:relative;width:1200px;height:1200px}
.page-label{position:absolute;color:#fff;font-weight:400;font-size:34px;letter-spacing:1px;transform:rotate(-90deg);transform-origin:left top;white-space:nowrap}
.page{position:absolute;width:370px;height:506px;background:var(--paper);overflow:hidden}
.page-header{position:absolute;left:0;top:0;width:100%;height:70px;background:var(--red);color:#fff}
.page-title{position:absolute;left:26px;top:36px;font-size:7.6px;font-weight:700;letter-spacing:.1px}
.page-address{position:absolute;left:26px;top:48px;font-size:6.8px;font-weight:400}
.brand{position:absolute;right:24px;top:26px;text-align:center;color:#fff}
.brand-mark{display:block;width:26px;height:20px;margin:0 auto 4px;border:2px solid #fff}
.brand-name{font-size:5.4px;font-weight:700;line-height:1.15}
.photo{position:absolute}
.photo-building{background:linear-gradient(180deg,#7fa6d6 0%,#cfdcec 45%,#b9a58c 62%,#5b7c3c 85%,#b3322c 100%)}
.photo-interior{background:linear-gradient(180deg,#d9d6c9 0%,#b89b6e 55%,#6e4a2a 100%)}
.photo-warehouse{background:linear-gradient(180deg,#6e6f74 0%,#b8b9bc 55%,#e6e6e6 100%)}
.photo-exterior{background:linear-gradient(180deg,#8fb1db 0%,#d9e2ec 40%,#bfa88a 60%,#cfcfcf 100%)}
.map-panel{position:absolute;left:25px;top:270px;width:321px;height:99px;border:1px solid var(--red);display:flex}
.map{width:186px;height:100%;background:linear-gradient(135deg,#e7e9e4,#d9dde0)}
.map-copy{flex:1;background:var(--red);color:#fff;font-size:6.6px;font-weight:700;text-align:center;line-height:1.45;padding-top:15px}
.specs{position:absolute;left:0;top:386px;width:100%;text-align:center;font-size:7.4px;line-height:1.52;color:var(--ink)}
.specs b{color:var(--red);font-weight:700}
.page-footer{position:absolute;left:0;bottom:0;width:100%;height:56px;background:var(--red)}
.footer-card{position:absolute;left:25px;bottom:24px;width:320px;height:36px;background:#fff;display:flex;align-items:center;gap:6px;padding:0 5px}
.footer-logo{width:34px;height:26px;background:var(--red);color:#fff;font-size:3.6px;font-weight:700;text-align:center;display:flex;align-items:center;justify-content:center;line-height:1.2}
.agent{width:64px;font-size:3.3px;line-height:1.4;color:var(--ink)}
.agent .agent-name{color:var(--red);font-weight:700}
.disclaimer{flex:1;font-size:3.2px;line-height:1.4;color:var(--muted)}
.floor-plan{position:absolute;left:28px;top:74px;width:184px;height:336px;border:1px solid #9aa;background:linear-gradient(180deg,var(--plan-blue) 0 27%,var(--plan-peach) 27% 100%)}
.spec-list{position:absolute;left:223px;top:84px;width:130px;font-size:5.6px;line-height:1.56;color:var(--muted)}
.spec-list b{color:var(--red);font-weight:700}
.spec-list h4{color:var(--red);font-size:5.8px;font-weight:700;margin:5px 0 3px}
.spec-list ul{list-style:none}
.spec-list li{position:relative;padding-left:7px}
.spec-list li::before{content:"";position:absolute;left:0;top:2.6px;width:3.5px;height:3.5px;background:var(--red)}
.plan-caption{position:absolute;left:0;top:421px;width:100%;text-align:center;font-size:7.8px;font-weight:700;color:var(--red)}
.notice-header{position:absolute;left:0;top:0;width:100%;height:77px;background:var(--red);color:#fff;text-align:center;padding-top:26px}
.notice-header .line1{font-size:6.4px;font-weight:700}
.notice-header .line2{font-size:5px;line-height:1.3;margin-top:4px}
.notice-header .line3{font-size:6.4px;font-weight:700;margin-top:4px}
.notice-col{position:absolute;top:80px;width:150px;font-size:3.4px;line-height:1.55;color:var(--muted)}
.notice-col h5{color:var(--red);font-size:6.2px;font-weight:700;margin:11px 0 4px}
.notice-col h6{color:var(--red);font-size:4.6px;font-weight:700;margin:11px 0 4px}
.drop-cap{float:left;color:var(--red);font-size:17px;font-weight:700;line-height:.9;margin-right:2px}
.acknowledge{position:absolute;left:0;top:300px;width:100%;text-align:center;font-size:4.8px;font-weight:700;color:var(--red);line-height:1.5}
.sign-row{position:absolute;left:26px;top:324px;width:318px;border-bottom:1px solid #bbb;height:12px;font-size:4.8px;color:var(--muted);padding-top:0}
.sign-row span{position:absolute;top:0}
.commission-bar{position:absolute;left:22px;top:370px;width:290px;height:18px;background:var(--red);color:#fff;font-size:3.4px;line-height:1.4;padding:3px 6px}
.housing-mark{position:absolute;left:318px;top:366px;width:22px;height:22px;border:2px solid #222}
.form-meta{position:absolute;font-size:5px;color:var(--ink);line-height:1.4}
.produced-band{position:absolute;left:0;bottom:0;width:100%;height:50px;background:var(--red)}
.produced-card{position:absolute;left:25px;bottom:24px;width:320px;height:22px;background:#fff;text-align:center;font-size:5.2px;font-weight:700;color:var(--ink);padding-top:7px}
.produced-card a{color:var(--red);text-decoration:none}
</style>
</head>
<body>
<div class="board">

  <div class="page-label" style="left:134px;top:374px">1ST PAGE</div>
  <div class="page-label" style="left:138px;top:938px">2ND PAGE</div>
  <div class="page-label" style="left:1038px;top:378px">3RD PAGE</div>
  <div class="page-label" style="left:1036px;top:938px">5TH PAGE</div>

  <!-- Page 1: listing cover -->
  <section class="page" style="left:219px;top:82px">
    <header class="page-header">
      <div class="page-title">FLEX INDUSTRIAL FOR SALE OR LEASE - HOUSTON, TEXAS</div>
      <div class="page-address">4810 CALDER WORKS BLVD., HOUSTON, TEXAS 77073</div>
      <div class="brand"><span class="brand-mark"></span><div class="brand-name">HALDEN REED<br>COMMERCIAL REAL ESTATE</div></div>
    </header>
    <div class="photo photo-building" role="img" aria-label="Exterior photo of the flex industrial building with monument sign and flower bed" style="left:25px;top:70px;width:321px;height:184px"></div>
    <div class="map-panel">
      <div class="map" role="img" aria-label="Area map showing the property location near IAH and The Woodlands"></div>
      <div class="map-copy">FLEX INDUSTRIAL - FOR SALE OR<br>LEASE WELL MAINTAINED<br>OWNER-OCCUPIED BUILDING<br>GREAT LOCATION<br>NEAR IAH &amp; THE WOODLANDS<br>EASY ACCESS TO HARDY,<br>IH-45 &amp; BELTWAY 8</div>
    </div>
    <div class="specs">
      <b>BUILDING AREA:</b> 11,820 SF (HCAD) | <b>LAND AREA:</b> 41,616 SF (HCAD)<br>
      <b>OFFICE BUILD-OUT:</b> APPROX. 2,820 SF (OWNER)<br>
      <b>LOADING:</b> THREE (3) GRADE-LEVEL<br>
      <b>EAVE HEIGHT:</b> APPROX. 22'<br>
      <b>OUTSIDE STORAGE: ROOM TO ADD FENCED YARD</b>
    </div>
    <footer class="page-footer"></footer>
    <div class="footer-card">
      <div class="footer-logo">HALDEN REED</div>
      <div class="agent"><span class="agent-name">HALDEN S. REED</span><br>PRESIDENT | CEO<br>PHONE: (281)555-0142<br>E-Mail: Marty@TLVKE.com<br>TREC BROKER LICENSE: 0000000</div>
      <div class="disclaimer">Information herein is from sources deemed reliable but is not guaranteed. Buyers should verify all details independently before any purchase or lease.</div>
    </div>
  </section>

  <!-- Page 3: floor plan and specifications -->
  <section class="page" style="left:634px;top:82px">
    <header class="page-header">
      <div class="page-title">FLEX INDUSTRIAL FOR SALE OR LEASE - HOUSTON, TEXAS</div>
      <div class="page-address">4810 CALDER WORKS BLVD., HOUSTON, TEXAS 77073</div>
      <div class="brand"><span class="brand-mark"></span><div class="brand-name">HALDEN REED<br>COMMERCIAL REAL ESTATE</div></div>
    </header>
    <div class="floor-plan" role="img" aria-label="Interior floor plan with office rooms along the top and about 9,000 SF warehouse space below"></div>
    <div class="spec-list">
      <div><b>FLEX INDUSTRIAL</b> - FOR SALE OR LEASE</div>
      <div><b>Year of Construction:</b> 2006</div>
      <div><b>Building Area:</b> 11,820 SF (HCAD)</div>
      <div><b>Land Area:</b> 41,616 SF (HCAD)</div>
      <div><b>Approximate Office Area:</b> 2,820 SF (Owner)</div>
      <div><b>Approximate Warehouse Area:</b> 9,000 SF (Owner)</div>
      <h4>Office Configuration:</h4>
      <ul>
        <li>(1) 14' X 16' Executive Office;</li>
        <li>(2) 14' X 12' Offices;</li>
        <li>(1) 10'8" X 12' Office;</li>
        <li>(1) Women's Restroom;</li>
        <li>(1) Men's Restroom;</li>
        <li>(1) Unisex Restroom;</li>
        <li>(1) 21'11" X 13' Conference Room;</li>
        <li>(1) Approximately 29' X 20' Training Room;</li>
        <li>(1) 26' X 11' Expanded Copy/Work Room;</li>
        <li>(1) 14' X 18'8" Break Room;</li>
        <li>(1) 16' X 12' Tech Supervision Room; (Multiple) Storage Closets;</li>
      </ul>
      <h4>Warehouse Configuration:</h4>
      <ul>
        <li>(3) Grade-Level Loading Doors;</li>
        <li>Approximately 22' Eave Height;</li>
        <li>3-Phase Power;</li>
        <li>Room For Fenced Outside Storage;</li>
        <li>Plenty of Parking;</li>
        <li>Large Dumpster Enclosure;</li>
      </ul>
    </div>
    <div class="plan-caption">INTERIOR LAYOUT NOT TO SCALE | DRAWING FOR SAMPLE PURPOSES ONLY</div>
    <footer class="page-footer"></footer>
    <div class="footer-card">
      <div class="footer-logo">HALDEN REED</div>
      <div class="agent"><span class="agent-name">HALDEN S. REED</span><br>PRESIDENT | CEO<br>PHONE: (281)555-0142<br>E-Mail: Marty@TLVKE.com<br>TREC BROKER LICENSE: 0000000</div>
      <div class="disclaimer">Information herein is from sources deemed reliable but is not guaranteed. Buyers should verify all details independently before any purchase or lease.</div>
    </div>
  </section>

  <!-- Page 2: photo gallery -->
  <section class="page" style="left:222px;top:634px;height:504px">
    <header class="page-header">
      <div class="page-title">FLEX INDUSTRIAL FOR SALE OR LEASE - HOUSTON, TEXAS</div>
      <div class="page-address">4810 CALDER WORKS BLVD., HOUSTON, TEXAS 77073</div>
      <div class="brand"><span class="brand-mark"></span><div class="brand-name">HALDEN REED<br>COMMERCIAL REAL ESTATE</div></div>
    </header>
    <div class="photo photo-exterior" role="img" aria-label="Building exterior with loading doors" style="left:30px;top:74px;width:151px;height:118px"></div>
    <div class="photo photo-interior" role="img" aria-label="Executive office with wood desk" style="left:190px;top:74px;width:151px;height:118px"></div>
    <div class="photo photo-interior" role="img" aria-label="Open office work area" style="left:30px;top:198px;width:151px;height:119px"></div>
    <div class="photo photo-interior" role="img" aria-label="Break room with cabinets" style="left:190px;top:198px;width:151px;height:119px"></div>
    <div class="photo photo-interior" role="img" aria-label="Private office with seating" style="left:30px;top:323px;width:151px;height:118px"></div>
    <div class="photo photo-warehouse" role="img" aria-label="Warehouse interior with high ceiling" style="left:190px;top:323px;width:151px;height:118px"></div>
    <footer class="page-footer" style="height:52px"></footer>
    <div class="footer-card" style="bottom:20px">
      <div class="footer-logo">HALDEN REED</div>
      <div class="agent"><span class="agent-name">HALDEN S. REED</span><br>PRESIDENT | CEO<br>PHONE: (281)555-0142<br>E-Mail: Marty@TLVKE.com<br>TREC BROKER LICENSE: 0000000</div>
      <div class="disclaimer">Information herein is from sources deemed reliable but is not guaranteed. Buyers should verify all details independently before any purchase or lease.</div>
    </div>
  </section>

  <!-- Page 5: brokerage services notice -->
  <section class="page" style="left:634px;top:634px;height:505px">
    <header class="notice-header">
      <div class="line1">APPROVED BY THE TEXAS REAL ESTATE COMMISSION FOR VOLUNTARY USE</div>
      <div class="line2">TEXAS LAW REQUIRES ALL REAL ESTATE LICENSEES TO GIVE THE FOLLOWING INFORMATION<br>ABOUT BROKERAGE SERVICES TO PROSPECTIVE BUYERS, TENANTS, SELLERS AND LANDLORDS.</div>
      <div class="line3">INFORMATION ABOUT BROKERAGE SERVICES</div>
    </header>
    <div class="notice-col" style="left:32px;top:82px">
      <p><span class="drop-cap">B</span>efore working with a real estate broker, you should know that the duties of a broker depend on whom the broker represents. Brokers must treat all parties honestly and fairly at all times.</p>
      <h5>IF THE BROKER REPRESENTS THE OWNER:</h5>
      <p>The broker becomes the owner's agent by entering into an agreement with the owner, usually through a written listing agreement. The broker must act in the owner's best interest.</p>
      <h5>IF THE BROKER REPRESENTS THE BUYER:</h5>
      <p>The broker becomes the buyer's agent by entering into an agreement to represent the buyer, usually through a written buyer representation agreement.</p>
      <h5>IF THE BROKER ACTS AS AN INTERMEDIARY:</h5>
      <p>A broker may act as an intermediary between the parties if the broker complies with state law.</p>
    </div>
    <div class="notice-col" style="left:193px;top:84px">
      <p>The broker must obtain the written consent of each party to act as an intermediary. The consent must state who will pay the broker and set out the broker's obligations.</p>
      <p style="margin-top:8px">(1) shall treat all parties honestly;<br>(2) may not disclose the lowest price the owner will accept;<br>(3) may not disclose the highest price the buyer will pay;<br>(4) may not disclose confidential information unless authorized.</p>
      <p style="margin-top:8px">With the parties' consent, a broker acting as an intermediary may appoint associates to communicate with and carry out instructions of each party.</p>
      <h6>IF YOU CHOOSE TO HAVE A BROKER REPRESENT YOU,</h6>
      <p>You should enter into a written agreement with the broker that clearly establishes the broker's obligations and your obligations, including how the broker will be paid.</p>
    </div>
    <div class="acknowledge">REAL ESTATE LICENSEE ASKS THAT YOU ACKNOWLEDGE RECEIPT OF THIS INFORMATION ABOUT<br>BROKERAGE SERVICES FOR THE LICENSEE'S RECORDS.</div>
    <div class="sign-row"><span style="left:0">Buyer, Seller, Landlord or Tenant</span><span style="left:164px">Date</span></div>
    <div class="commission-bar">Real estate brokers and salespersons are licensed by the state commission. Questions or complaints may be sent to P.O. Box 10000, Austin, Texas.</div>
    <div class="housing-mark" role="img" aria-label="Equal housing badge"></div>
    <div class="form-meta" style="left:222px;top:398px">01A</div>
    <div class="form-meta" style="left:300px;top:398px;text-align:right">TREC No. OP-K<br>Page 1 of 1</div>
    <div class="form-meta" style="left:30px;top:418px">(TAR-2501) 1/1/96</div>
    <div class="form-meta" style="left:30px;top:429px">Halden Reed Commercial Real Estate P.O. Box 550210 The Woodlands, TX 77393<br>Phone: (281)555-0142 | Fax: (281)555-0143 | Halden Reed</div>
    <div class="form-meta" style="left:290px;top:429px">Ansel - Corin</div>
    <footer class="produced-band"></footer>
    <div class="produced-card">Produced with FormDesk by Northline Forms 2200 Ashby Lane, Dearborn, Michigan 48120 <a>www.northlineforms.com</a></div>
  </section>

</div>
</body>
</html>
```